Flyer-Design für Ferienhaus auf Sylt
Zielgruppe
Ferienhaus auf Sylt im ruhigen und traditionellen Ort Archsum. Zielgruppe ruhe- und erholungssuchende Erwachsene, Familien mit Kind und evtl. mit Hund. Ferienhaus 'klein, aber fein' in ruhiger Lager mit großem Grundstück.
Homepage: duenenkate-wiesmoor.de
Aufgabenstellung
Format DIN LANG / 4 Seiten: Es sollen keine Saisonzeiten und auch keine Preise genannt werden. Es soll nur genannt werden, dass das Haus ab 50 EUR / Tag gemietet werden kann. Bitte nicht die vollständige Adresse des Objektes angeben, lediglich „Sylt-Archsum“. Kontakdtaen bitte auf der Rückseite nennen (siehe Homepage). Kontaktaufnahme bevorzugt per Mail / Anfrageformular v. Homepage. Gerne meine Bilder nutzen, bin aber auch offen für 2-3 Bilder aus dem Stock. Kleine Texte formulieren und gerne mehrere Bilder des Hauses zeigen.

```html
<!DOCTYPE html>
<html lang="de">
<head>
<meta charset="utf-8">
<title>Dünenkate – Ausstattung</title>
<link rel="stylesheet" href="https://fonts.googleapis.com/css2?family=Montserrat:wght@700&family=Gudea:wght@400;700&display=swap">
<style>
  :root{
    --paper:#f3f3f2;
    --plank-line:#e6e6e4;
    --ink:#262626;
    --ink-soft:#2f2f2f;
    --accent:#1f5596;
    --photo-wood:#b98f5d;
    --photo-white:#e9e9e6;
    --photo-tile:#dcdcd8;
    --photo-sky:#7fb0d8;
    --photo-grass:#5f9a3a;
  }
  *{margin:0;padding:0;box-sizing:border-box}
  html,body{width:1200px;height:1200px;overflow:hidden}
  body{
    background:
      repeating-linear-gradient(180deg, transparent 0 163px, var(--plank-line) 163px 168px),
      var(--paper);
    font-family:"Gudea",sans-serif;
    color:var(--ink-soft);
    position:relative;
  }
  .floor-title{
    position:absolute;
    font-family:"Montserrat",sans-serif;
    font-weight:700;
    font-size:31px;
    line-height:1;
    letter-spacing:-0.3px;
    color:var(--ink);
  }
  .photo{position:absolute;width:257px}
  .photo--living{background:linear-gradient(180deg,#dfe2ea 0%,#c9cbd6 45%,var(--photo-wood) 100%)}
  .photo--dining{background:linear-gradient(180deg,#efefec 0%,#dcd8cf 55%,var(--photo-wood) 100%)}
  .photo--kitchen{background:linear-gradient(180deg,#e8e1d3 0%,var(--photo-white) 55%,#e4e0d8 100%)}
  .photo--shower{background:linear-gradient(160deg,var(--photo-white) 0%,#f3f3f1 50%,var(--photo-tile) 100%)}
  .photo--bedroom{background:linear-gradient(180deg,#f1f1ef 0%,#d8c7ab 55%,var(--photo-wood) 100%)}
  .photo--kidsroom{background:linear-gradient(180deg,#ecebe8 0%,#e0d4c0 50%,var(--photo-wood) 100%)}
  .photo--bath{background:linear-gradient(180deg,#f2f2f0 0%,#e2ddd4 55%,#6f6f6f 100%)}
  .photo--terrace{background:linear-gradient(180deg,var(--photo-sky) 0%,#9e5a45 35%,#c9c7c2 65%,var(--photo-grass) 100%)}
  .copy{
    position:absolute;
    white-space:nowrap;
    font-size:16.6px;
    line-height:18.8px;
    letter-spacing:0.4px;
  }
  .copy strong{font-weight:700}
  .divider{position:absolute;left:629px;top:959px;width:514px;height:4px;background:var(--accent)}
  .info{position:absolute;left:629px;width:520px;font-size:16.6px;line-height:18.8px;letter-spacing:0.2px}
  .info h3{font-family:"Montserrat",sans-serif;font-weight:700;font-size:15px;letter-spacing:0.3px;color:var(--ink);line-height:18px}
  .contact{
    position:absolute;right:630px;top:1110px;text-align:right;
    font-size:16.6px;line-height:19px;letter-spacing:0.2px;
  }
  .contact .site{font-family:"Montserrat",sans-serif;font-weight:700;font-size:14.5px;letter-spacing:0.3px;color:var(--ink)}
</style>
</head>
<body>

  <h1 class="floor-title" style="left:55px;top:54px">ERDGESCHOSS</h1>
  <div class="photo photo--living" style="left:57px;top:84px;height:193px" role="img" aria-label="Foto: helles Wohnzimmer mit blauer Ecksofa-Couch und Holztisch"></div>
  <p class="copy" style="left:343px;top:84px">Lichtdurchflutetes<br>Wohnzimmer mit ausziehbarer<br>Couch (zwei Schlafgelegen-<br>heiten), Fußbodenheizung,<br>Innenjalousien mit Sichtschutz<br>und Verdunklung, Flachbild-<br>fernseher (Kabelfernsehen) mit<br>DVD-Player, Stereoanlage mit<br>CD-Player, USB- und MP3-<br>Player-Anschluss</p>
  <div class="photo photo--dining" style="left:57px;top:283px;height:191px" role="img" aria-label="Foto: Essbereich mit Holztisch, Stühlen, Fernseher und Sideboard"></div>

  <div class="photo photo--kitchen" style="left:57px;top:495px;height:171px" role="img" aria-label="Foto: offene Einbauküche in Cremeweiß"></div>
  <p class="copy" style="left:343px;top:495px"><strong>Offene Küche</strong><br>Moderne Einbauküche mit<br>ausreichend Geschirr und<br>Besteck, Geschirrspüler,<br>Mikrowelle, Backofen,<br>Kapselino von Bohnenhof,<br>Wasserkocher, Kaffeemaschine<br>und Toaster</p>

  <div class="photo photo--shower" style="left:57px;top:686px;height:343px" role="img" aria-label="Foto: weiß gefliestes Badezimmer mit Glasdusche und WC"></div>
  <p class="copy" style="left:343px;top:686px"><strong>Badezimmer mit Dusche</strong>,<br>einem Waschbecken, WC sowie<br>Fußbodenheizung</p>

  <h1 class="floor-title" style="left:627px;top:54px">OBERGESCHOSS</h1>
  <div class="photo photo--bedroom" style="left:629px;top:84px;height:193px" role="img" aria-label="Foto: Schlafzimmer mit Doppelbett unter Dachschräge"></div>
  <p class="copy" style="left:914px;top:84px">Schlafzimmer mit einem<br>Doppelbett und geräumigem<br>Kleiderschrank und einem<br>Flachbildfernseher an der<br>Wand</p>

  <div class="photo photo--kidsroom" style="left:629px;top:297px;height:193px" role="img" aria-label="Foto: Kinderzimmer mit ausziehbarem Bett und Kommode"></div>
  <p class="copy" style="left:914px;top:298px">Zweites Schlafzimmer/Kinder-<br>zimmer mit Fußbodenheizung<br>sowie einem ausziehbaren<br>Doppelbett</p>

  <div class="photo photo--bath" style="left:629px;top:511px;height:192px" role="img" aria-label="Foto: modernes Badezimmer mit Waschmaschine, WC und Waschtisch"></div>
  <p class="copy" style="left:914px;top:511px">Badezimmer mit Fußboden-<br>heizung, WC, Waschbecken und<br>Waschmaschine (modernisiert<br>November 2019)</p>

  <h1 class="floor-title" style="left:627px;top:718px">TERRASSE</h1>
  <div class="photo photo--terrace" style="left:629px;top:748px;height:192px" role="img" aria-label="Foto: Klinkerhaus mit Süd-Terrasse, Gartenmöbeln und Strandkorb"></div>
  <p class="copy" style="left:914px;top:750px"><strong>Schöne Süd-Terrasse</strong> mit<br>ausreichend Gartenmöbeln,<br>Strandkorb und großer<br>Liegewiese</p>

  <div class="divider"></div>

  <div class="info" style="top:979px">
    <h3>PKW-STELLPLATZ</h3>
    <p>Ein PKW-Stellplatz befindet sich auf dem Grundstück direkt am Haus.</p>
  </div>
  <div class="info" style="top:1035px">
    <h3>WLAN</h3>
    <p>WLAN-Anschluss und Telefonverbindungen innerhalb Deutschlands sind kostenlos.</p>
  </div>
  <div class="info" style="top:1110px">
    <h3>KONTAKTLOSE ANREISE</h3>
    <p>Das Haus einfach mit persönlichem PIN-Code öffnen und betreten.</p>
  </div>

  <div class="contact">
    <p>Kontaktaufnahme bevorzugt per Mail / Anfrageformular</p>
    <p class="site">WWW.DUENENKATE-WIESMOOR.DE</p>
  </div>

</body>
</html>
```